Redesigning of the packaging for 4 GOLDEN HEARTH gourmet breads

We need new designs for our range of four gourmet sliced breads, called GOLDEN HEARTH. These breads are prepared with specially selected ingredients sourced from several countries and with extreme focus on quality, health and indulgent pleasure. The Golden Hearth brand aims to solve the boring and bland nature of white breads and comes in several flavours such as coconut, seeds & nuts, exotic fruits and vegetables, buttermilk, chocolate, etc.
The Golden Hearth brand positioning statement is JOY IN EVERY SLICE
The current packaging designs are still quite attractive which makes it a difficult decision, but we know it's time for a rebrand, and therefore we really want the best possible designs - ONLY THE BEST!
GOLDEN HEARTH currently comprises three 'sister' products and one new addition named as follows:
1. Golden Hearth - buttermilk dream (yellow color)
2. Golden Hearth - cocoa swirl (brown & orange color)
3. Golden Hearth - tropic coconut (green & cream color)
4. Hearth Tots - (kiddies' style - This is a kiddies bread)
[Some pictures of the current packaging are attached, alongside with the content, layout and dimensions which should be used for the new designs, including ingredients, addresses, etc. Check the file 'Back view with ingredients and contents.pdf'; 'Layout and Dimensions of current Golden Hearth Packaging.pdf]
5. The logo may or may not be modified. (Golden Hearth Logo.pdf)
Key points to note:
- Demographic: The target audience is mainly young and middle aged from the middle to upper economic class
- Psychographic: Health conscious, Class conscious, Family focused consumers, Environment and Sustainable development minded consumers
- The designs will be similar in style for the 3 variants but be differentiated by colours and content
- The fonts and the overall design should be modern, playful and inviting.
- The content of the packaging is in the attachments
- Total designs - 4 designs.
Target Market(s)
The target market is kids, teens, young adults. Middle to upper economic class. Premium segment, lifestyle conscious consumers.
Industry/Entity Type
Bakery
Colors
Designer to choose colors to be used in the design.
Look and feel

```html
<!DOCTYPE html>
<html lang="en">
<head>
<meta charset="utf-8">
<title>Golden Hearth – Buttermilk Dream Pack</title>
<link href="https://fonts.googleapis.com/css2?family=Kalam:wght@700&family=Roboto+Condensed:wght@700;900&display=swap" rel="stylesheet">
<style>
  :root{
    --bg:#eceef0;
    --sun:#fff38a;
    --yellow:#f6d31c;
    --orange:#ef8a16;
    --deep-orange:#e06a10;
    --brand:#7a1410;
    --ribbon:#c8221c;
    --ribbon-dark:#8e1512;
    --tan:#c4862e;
    --ink:#1a1a1a;
    --crust:#c7773a;
    --crumb:#e6b27e;
    --tab:#e8731c;
    --film:#d9dde0;
    --white:#ffffff;
  }
  *{box-sizing:border-box;margin:0;padding:0}
  html,body{width:1200px;height:846px;overflow:hidden;background:var(--bg)}
  .canvas{position:relative;width:1200px;height:846px}
  .pack{position:absolute;left:40px;top:170px;width:1120px;height:500px}

  .label{
    position:absolute;left:0;top:0;width:640px;height:500px;
    border-radius:44px 0 0 44px;overflow:hidden;
    background:radial-gradient(circle at 58% 52%,var(--white) 0%,var(--sun) 12%,var(--yellow) 38%,var(--orange) 78%,var(--deep-orange) 100%);
  }
  .tagline{
    position:absolute;left:150px;top:50px;
    font-family:'Kalam',cursive;font-weight:700;font-size:46px;line-height:1.2;color:var(--ink);
    white-space:nowrap;
  }
  .badge{position:absolute;left:56px;top:112px;width:80px;height:80px;border-radius:50%;
    background:var(--brand);border:6px solid #e9b44a}
  .brand-name{
    position:absolute;left:150px;top:188px;
    font-family:'Roboto Condensed',sans-serif;font-weight:900;font-size:70px;line-height:.95;
    color:var(--brand);text-transform:uppercase;
  }
  .illustration{position:absolute;left:430px;top:150px;width:180px;height:160px;border-radius:16px;
    background:linear-gradient(160deg,#5f8f3c 0%,#9aa23c 40%,#e3a23a 75%,#f2c05a 100%)}
  .ribbon{position:absolute;left:290px;top:330px;width:340px;height:56px}
  .ribbon svg{position:absolute;inset:0;width:100%;height:100%}
  .ribbon-text{position:absolute;left:28px;right:28px;top:0;bottom:4px;display:flex;align-items:center;justify-content:center;
    font-family:'Roboto Condensed',sans-serif;font-weight:700;font-size:27px;color:var(--white);letter-spacing:.3px;white-space:nowrap}
  .promise{position:absolute;left:140px;top:410px;font-family:'Roboto Condensed',sans-serif;font-weight:700;
    font-size:20px;line-height:1.05;color:var(--tan)}
  .promise strong{font-size:30px;display:block}
  .benefits{position:absolute;left:340px;top:400px;display:flex;gap:26px}
  .benefit{width:72px;height:72px;border-radius:12px;background:var(--white);border:4px solid var(--tan);
    display:flex;align-items:center;justify-content:center}

  .window{position:absolute;left:640px;top:0;width:300px;height:500px;
    background:linear-gradient(180deg,var(--crumb) 0%,#d99a5c 50%,var(--crust) 100%);
    border-radius:0 30px 30px 0}
  .heart{position:absolute;left:600px;top:30px;width:150px;height:132px}
  .neck{position:absolute;left:940px;top:200px;width:40px;height:100px;background:var(--film)}
  .tab{position:absolute;left:980px;top:40px;width:140px;height:420px;
    background:linear-gradient(90deg,var(--ribbon) 0 14px,var(--tab) 14px 100%)}
</style>
</head>
<body>
<div class="canvas">
  <div class="pack">
    <section class="label">
      <div class="tagline">Joy in every slice...</div>
      <div class="badge" aria-hidden="true"></div>
      <h1 class="brand-name">Golden<br>Hearth</h1>
      <div class="illustration" role="img" aria-label="Illustration of a palm tree, pineapple, banana, orange, apple and bread slices"></div>
      <div class="ribbon">
        <svg viewBox="0 0 340 56" preserveAspectRatio="none" aria-hidden="true">
          <polygon points="0,10 22,30 0,50 34,50 34,10" fill="var(--ribbon-dark)"/>
          <polygon points="340,10 318,30 340,50 306,50 306,10" fill="var(--ribbon-dark)"/>
          <rect x="20" y="2" width="300" height="48" rx="4" fill="var(--ribbon)"/>
        </svg>
        <div class="ribbon-text">BUTTERMILK DREAM</div>
      </div>
      <p class="promise"><strong>Bread</strong>that you and your<br>family will love</p>
      <div class="benefits">
        <div class="benefit" aria-label="Meal">
          <svg width="52" height="40" viewBox="0 0 52 40"><circle cx="26" cy="20" r="14" fill="none" stroke="var(--tan)" stroke-width="4"/><circle cx="26" cy="20" r="7" fill="var(--tan)"/><rect x="3" y="4" width="4" height="32" rx="2" fill="var(--tan)"/><rect x="45" y="4" width="4" height="32" rx="2" fill="var(--tan)"/></svg>
        </div>
        <div class="benefit" aria-label="Heart health">
          <svg width="52" height="46" viewBox="0 0 52 46"><path d="M24 42 C4 28 2 18 6 10 C10 2 20 2 24 10 C28 2 38 2 42 10 C46 18 44 28 24 42Z" fill="var(--tan)"/><circle cx="38" cy="34" r="9" fill="var(--white)" stroke="var(--tan)" stroke-width="3"/><path d="M38 29 V34 H42" stroke="var(--tan)" stroke-width="2.5" fill="none"/></svg>
        </div>
        <div class="benefit" aria-label="Strength">
          <svg width="46" height="46" viewBox="0 0 46 46"><path d="M10 40 L10 10 Q12 4 18 6 L22 10 L18 14 L16 20 Q26 14 36 22 Q42 30 36 38 Q26 42 10 40Z" fill="var(--tan)"/></svg>
        </div>
      </div>
    </section>
    <div class="window" role="img" aria-label="Clear window showing the sliced buttermilk loaf"></div>
    <svg class="heart" viewBox="0 0 170 150" aria-hidden="true">
      <path d="M85 140 C25 95 8 62 20 34 C34 6 70 8 85 36 C100 8 136 6 150 34 C162 62 145 95 85 140Z" fill="none" stroke="var(--ribbon)" stroke-width="6"/>
    </svg>
    <div class="neck" aria-hidden="true"></div>
    <div class="tab" role="img" aria-label="Orange bag closure with wheat pattern"></div>
  </div>
</div>
</body>
</html>
```